Corporate travel agency website design

Hello I need a website design that will look professional. I want that anyone that gos on our site understands that we are a large successful company. I want it to be up to par with other large companies. The site should be sleek and neat.
Below I will attach my logo. A recent one page add I made and content for my add that will be used for the website.

```html
<!DOCTYPE html>
<html lang="en">
<head>
<meta charset="utf-8">
<title>Meridian Travel – Business Travel Reinvented</title>
<link href="https://fonts.googleapis.com/css2?family=Poppins:wght@300;400;500&family=Questrial&display=swap" rel="stylesheet">
<style>
:root{
  --navy:#0b1a33;
  --nav:#07122a;
  --page:#eef7fb;
  --band:#c7ebf8;
  --ice:#cfeefb;
  --card:#111923;
  --ink:#1a1c26;
  --muted:#3a3f4a;
  --white:#ffffff;
  --icon:#9fb3c4;
}
*{margin:0;padding:0;box-sizing:border-box}
html,body{width:1200px;height:4073px;overflow:hidden;background:var(--page)}
body{font-family:"Poppins",sans-serif;color:var(--ink)}
.page{position:relative;width:1200px;height:4073px;overflow:hidden}
.backdrop{position:absolute;left:0;top:0}
.abs{position:absolute}
.heading{font-family:"Questrial",sans-serif;font-weight:400;color:var(--ink)}
.copy{font-size:16px;line-height:27.3px;font-weight:300;color:var(--ink);text-align:justify}

/* nav */
.brand{position:absolute;display:flex;align-items:center;gap:10px;font-family:"Poppins",sans-serif;font-weight:400;letter-spacing:2px}
.brand .dot{width:12px;height:12px;border-radius:50%;background:currentColor;flex:none}
.brand-top{left:130px;top:38px;color:#dfe8f2;font-size:15px}
.nav-links{position:absolute;top:48px;left:713px;display:flex;gap:45px;font-size:15px;color:#e8eef6}
.nav-links a{color:inherit;text-decoration:none}
.nav-links .current{font-weight:500}

/* hero */
.hero-welcome{left:120px;top:252px;font-family:"Questrial",sans-serif;font-size:27px;color:var(--white)}
.hero-title{left:118px;top:284px;font-family:"Questrial",sans-serif;font-size:47px;letter-spacing:1px;color:var(--white)}
.hero-sub{left:120px;top:344px;font-size:16px;letter-spacing:1px;color:#dbe6f0}
.btn-start{left:120px;top:384px;width:139px;height:44px;border-radius:6px;background:var(--ice);color:var(--ink);font-size:16px;display:flex;align-items:center;justify-content:center}

/* sections */
.h2{font-size:35px}

/* features */
.card{position:absolute;width:308px;height:178px}
.card svg{position:absolute;left:0;top:0}
.card .icon{position:absolute;left:44px;top:56px;width:58px;height:62px;border-radius:8px;background:var(--icon);opacity:.85}
.card .label{position:absolute;left:136px;top:0;height:178px;display:flex;align-items:center;font-family:"Questrial",sans-serif;font-size:23px;line-height:28px;color:var(--white)}

/* contact */
.contact-list{left:120px;font-size:20px;color:var(--ink);display:flex;gap:20px;align-items:flex-start}
.contact-list svg{flex:none;margin-top:5px}
.field-label{position:absolute;left:643px;font-size:16px;color:var(--white)}
.field{position:absolute;left:634px;width:397px;background:var(--white);border-radius:5px;font-size:11px;color:#8a8f98;padding:11px 14px}
.btn-submit{position:absolute;left:634px;top:3640px;width:106px;height:39px;border-radius:5px;background:var(--white);font-size:15px;color:var(--ink);display:flex;align-items:center;justify-content:center}

/* footer */
.brand-foot{left:158px;top:3940px;color:var(--ink);font-size:17px}
.foot-about{left:400px;top:3880px;width:660px;font-size:16px;line-height:27px;font-weight:300;color:#2a2f3a}
.foot-links{position:absolute;top:3958px;left:403px;display:flex;gap:42px;font-size:15px;font-weight:500;color:var(--ink)}
.follow{position:absolute;left:887px;top:3953px;display:flex;align-items:center;gap:14px;font-size:16px;color:var(--ink)}
.follow .soc{width:14px;height:14px;border-radius:50%;background:var(--ink)}
.rule{position:absolute;left:0;top:4011px;width:1200px;height:1px;background:#9aa6b2}
.legal{position:absolute;top:4026px;width:1200px;text-align:center;font-size:12px;font-weight:300;color:#3a3f4a}
</style>
</head>
<body>
<div class="page">

  <svg class="backdrop" width="1200" height="4073" viewBox="0 0 1200 4073">
    <defs>
      <linearGradient id="heroGrad" x1="0" y1="0" x2="1" y2="1">
        <stop offset="0" stop-color="#0c1c38"/>
        <stop offset="1" stop-color="#0a1830"/>
      </linearGradient>
    </defs>
    <polygon points="0,0 1200,0 1200,664 0,593" fill="url(#heroGrad)"/>
    <rect x="0" y="0" width="1200" height="103" fill="var(--nav)"/>
    <polygon points="0,1186 1200,1241 1200,1632 0,1576" fill="var(--band)"/>
    <polygon points="0,2051 1200,2108 1200,2609 0,2550" fill="var(--band)"/>
    <polygon points="588,3217 1200,3236 1200,3744 588,3712" fill="var(--card)"/>
    <path d="M588 3217 L588 3712" stroke="none"/>
    <polygon points="0,3783 1200,3839 1200,4011 0,4011" fill="var(--band)"/>
  </svg>

  <!-- navigation -->
  <div class="brand brand-top"><span class="dot"></span>MERIDIAN TRAVEL</div>
  <nav class="nav-links">
    <a class="current" href="#">Home</a><a href="#">About</a><a href="#">Services</a><a href="#">Contact</a>
  </nav>

  <!-- hero -->
  <svg class="abs" style="left:500px;top:103px" width="700" height="562" viewBox="0 0 700 562">
    <defs>
      <linearGradient id="heroPhoto" x1="0" y1="0" x2="1" y2="1">
        <stop offset="0" stop-color="#1e3f5c"/>
        <stop offset=".55" stop-color="#2f5f7c"/>
        <stop offset="1" stop-color="#102a44"/>
      </linearGradient>
    </defs>
    <path d="M40 0 C5 120 20 380 170 500 C230 548 300 560 380 560 L700 560 L700 0 Z" fill="none" stroke="var(--ice)" stroke-width="6"/>
    <path role="img" aria-label="Photo of a businessman holding a model airplane over map pins" d="M52 0 C20 120 36 370 180 488 C240 536 310 552 390 556 L700 560 L700 0 Z" fill="url(#heroPhoto)"/>
  </svg>
  <div class="abs hero-welcome">Welcome to</div>
  <div class="abs hero-title">MERIDIAN TRAVEL</div>
  <div class="abs hero-sub">Business Travel Reinvented</div>
  <div class="abs btn-start">Get Started</div>

  <!-- why choose -->
  <svg class="abs" style="left:72px;top:752px" width="360" height="345" viewBox="0 0 360 345">
    <defs>
      <linearGradient id="airport" x1="0" y1="0" x2="0" y2="1">
        <stop offset="0" stop-color="#5b86b6"/>
        <stop offset=".5" stop-color="#e8f2fb"/>
        <stop offset="1" stop-color="#2b3a4c"/>
      </linearGradient>
    </defs>
    <path d="M40 60 C110 -10 280 -10 335 70 C375 140 320 250 230 315 C170 355 90 330 40 250 C0 185 -5 105 40 60 Z" fill="var(--ice)"/>
    <path role="img" aria-label="Photo of business travellers walking through an airport terminal" d="M30 60 C95 -2 255 0 310 65 C350 130 300 245 215 305 C160 343 85 320 37 245 C0 185 -8 100 30 60 Z" fill="url(#airport)"/>
  </svg>
  <h2 class="abs heading h2" style="left:479px;top:733px">Why Choose Meridian Travel?</h2>
  <p class="abs copy" style="left:479px;top:800px;width:601px">Meridian Travel is a global leader in business travel management services. We drive savings, efficiency, and unparalleled service to businesses and their travelers all around the world. If you are looking for a tailored travel managed solution focused on offering white glove service and fulfilling your individual preferences ,while delivering customer excellence, you've come to the right place. At Meridian Travel, our mission is to have you focus on your day to day business while we handle all of the logistics and details for the most successful all encompassing travel experience. From emergency passport arrangements to last minute cancellations, re-bookings, and other intricate travel challenges, Meridian Travel is well versed in handling the routine array of travel services, as well as solving any travel related issue that might arise.</p>

  <!-- unparalleled service -->
  <h2 class="abs heading h2" style="left:120px;top:1286px">Unparalled Service</h2>
  <p class="abs copy" style="left:120px;top:1352px;width:601px">Meridian Travel is famous for our concierge style approach to travel. From detailed planning, to commercial or private air travel, transportation, including car rentals, chauffers, busses for larger groups, hotels, all styles of lodging accomodations, special event planning and more, Meridian Travel is like having your own personal or corporate travel butler.</p>
  <svg class="abs" style="left:787px;top:1293px" width="413" height="282" viewBox="0 0 413 282">
    <path role="img" aria-label="Photo of a smiling travel consultant holding passports and tickets at a meeting" d="M24 0 L413 16 L413 282 L24 262 Q0 260 0 236 L0 24 Q0 0 24 0 Z" fill="#6f7d8c"/>
  </svg>

  <!-- efficiency -->
  <svg class="abs" style="left:0;top:1673px" width="400" height="282" viewBox="0 0 400 282">
    <path role="img" aria-label="Photo of a passport and boarding pass being handed across a desk" d="M0 0 L372 16 Q400 18 400 44 L400 252 Q400 282 372 280 L0 260 Z" fill="#8b8f94"/>
  </svg>
  <h2 class="abs heading h2" style="left:479px;top:1683px">Efficiency</h2>
  <p class="abs copy" style="left:479px;top:1748px;width:601px">Time is your most valuable tool! Our goal at Meridian Travel is to have your employees' complete focus be on your core business, while having us handle all the logistics for their travel. One of the most appreciated services we offer is the management of travel headaches. Unforeseen circumstances such as cancellations, missed flights, cancelled flights, last minute bookings or changed plans, can take hours to rectify. Meridian Travel handles all of these tedious repositionings expeditiously, saving your employees precious time. Give your company a competitive edge by having Meridian Travel handle your team's travel arrangements.</p>

  <!-- budget -->
  <h2 class="abs heading h2" style="left:120px;top:2151px">Budget and Travel Spend Reporting</h2>
  <p class="abs copy" style="left:120px;top:2216px;width:601px">Having a travel management service will ensure that your company enforces corporate compliance and maintains control over travel decisions. This ensures that your employees stick to your budget, which in turn will protect your bottom line. Travel expenses can be costly. Having a savvy and experienced corporate travel manager who can access deep discounts not available to the public will ensure your travel is booked across the board at the lowest prices expenses are kept under control. Travel reporting is critical to optimizing budgets, streamlining expense reports, and recognizing key trends. Meridian-Travel customizes travel spend reports, by team, project, department etc, so companies can accurately track travel expenses, and make critical decisions based on the spend.</p>
  <svg class="abs" style="left:787px;top:2205px" width="413" height="280" viewBox="0 0 413 280">
    <path role="img" aria-label="Photo of a toy car beside stacks of coins and a calculator" d="M24 0 L413 16 L413 280 L24 262 Q0 260 0 236 L0 24 Q0 0 24 0 Z" fill="#5c6f86"/>
  </svg>

  <!-- feature cards -->
  <div class="card" style="left:84px;top:2681px">
    <svg width="308" height="178" viewBox="0 0 308 178"><path d="M12 0 L296 12 Q308 12 308 24 L308 166 Q308 178 296 178 L12 170 Q0 170 0 158 L0 12 Q0 0 12 0 Z" fill="var(--card)"/></svg>
    <div class="icon" role="img" aria-label="Glove icon"></div>
    <div class="label">White Glove<br>Service</div>
  </div>
  <div class="card" style="left:446px;top:2681px">
    <svg width="308" height="178" viewBox="0 0 308 178"><path d="M12 0 L296 12 Q308 12 308 24 L308 166 Q308 178 296 178 L12 170 Q0 170 0 158 L0 12 Q0 0 12 0 Z" fill="var(--card)"/></svg>
    <div class="icon" role="img" aria-label="Policy document with airplane icon"></div>
    <div class="label">Corp<br>travel policy<br>compliance</div>
  </div>
  <div class="card" style="left:808px;top:2681px">
    <svg width="308" height="178" viewBox="0 0 308 178"><path d="M12 0 L296 12 Q308 12 308 24 L308 166 Q308 178 296 178 L12 170 Q0 170 0 158 L0 12 Q0 0 12 0 Z" fill="var(--card)"/></svg>
    <div class="icon" role="img" aria-label="Expense report icon"></div>
    <div class="label">Streamlined<br>expense<br>reports</div>
  </div>
  <div class="card" style="left:266px;top:2915px">
    <svg width="308" height="178" viewBox="0 0 308 178"><path d="M12 0 L296 12 Q308 12 308 24 L308 166 Q308 178 296 178 L12 170 Q0 170 0 158 L0 12 Q0 0 12 0 Z" fill="var(--card)"/></svg>
    <div class="icon" role="img" aria-label="Service management icon"></div>
    <div class="label">Full Service<br>travel<br>management<br>program</div>
  </div>
  <div class="card" style="left:628px;top:2915px">
    <svg width="308" height="178" viewBox="0 0 308 178"><path d="M12 0 L296 12 Q308 12 308 24 L308 166 Q308 178 296 178 L12 170 Q0 170 0 158 L0 12 Q0 0 12 0 Z" fill="var(--card)"/></svg>
    <div class="icon" role="img" aria-label="Wallet with currency icon"></div>
    <div class="label">Unparallel<br>Savings</div>
  </div>

  <!-- contact -->
  <h2 class="abs heading h2" style="left:120px;top:3267px">Contact Us</h2>
  <p class="abs" style="left:123px;top:3330px;width:390px;font-size:14px;line-height:27px;font-weight:300;color:var(--ink)">Lorem ipsum dolor sit amet, consectetur adipiscing elit, sed do eiusmod tempor incididunt ut labore et dolore magna aliqua. Quis ipsum suspendisse ultrices gravida.</p>
  <div class="abs contact-list" style="top:3456px">
    <svg width="16" height="20" viewBox="0 0 16 20"><path d="M8 0 C3.6 0 0.5 3.2 0.5 7.3 C0.5 12.5 8 20 8 20 C8 20 15.5 12.5 15.5 7.3 C15.5 3.2 12.4 0 8 0 Z M8 10 A2.8 2.8 0 1 1 8 4.4 A2.8 2.8 0 1 1 8 10 Z" fill="var(--ink)"/></svg>
    <div style="line-height:27px">#1, Sample Street, Sample<br>City - 765327</div>
  </div>
  <div class="abs contact-list" style="top:3534px">
    <svg width="18" height="18" viewBox="0 0 24 24"><path d="M6.6 2.5 L9.5 6.5 L7.8 8.8 C8.9 11.2 12.8 15.1 15.2 16.2 L17.5 14.5 L21.5 17.4 L19.5 21 C11 21 3 13 3 4.5 Z" fill="none" stroke="var(--ink)" stroke-width="1.6" stroke-linejoin="round"/></svg>
    <div>(1) 888-888-8888</div>
  </div>
  <div class="abs contact-list" style="top:3586px">
    <svg width="17" height="13" viewBox="0 0 17 13"><rect x="0" y="0" width="17" height="13" rx="1.5" fill="var(--ink)"/><path d="M1 1.5 L8.5 7 L16 1.5" fill="none" stroke="var(--page)" stroke-width="1.4"/></svg>
    <div>info@meridiantravel.com</div>
  </div>

  <div class="field-label" style="top:3253px">Your Name</div>
  <div class="field" style="top:3285px;height:51px">Your Name</div>
  <div class="field-label" style="top:3341px">Phone Number</div>
  <div class="field" style="top:3372px;height:51px">Phone Number</div>
  <div class="field-label" style="top:3430px">Email</div>
  <div class="field" style="top:3458px;height:50px">Email</div>
  <div class="field-label" style="top:3510px">Message</div>
  <div class="field" style="top:3538px;height:82px">Message</div>
  <div class="btn-submit">Submit</div>

  <!-- footer -->
  <div class="brand brand-foot"><span class="dot"></span>MERIDIAN TRAVEL</div>
  <p class="abs foot-about">Meridian Travel is a global leader in business travel management services. We drive savings, efficiency, and unparalleled service to businesses and their travelers all around the world.</p>
  <nav class="foot-links"><span>Home</span><span>About</span><span>Services</span><span>Contact</span></nav>
  <div class="follow">Follow us : <span class="soc"></span><span class="soc"></span><span class="soc"></span></div>
  <div class="rule"></div>
  <div class="legal">© copyrights 2023 Meridian Travel | &nbsp;All Rights Reserved</div>

</div>
</body>
</html>
```